New Letterhead

Improve the attached letterhead to make it more alive and corporate class using the company colors in the two companies logos available on the two companies website.

Industry/Entity Type

Construction Company

Requirements
Must have
• colours of the two logod
Nice to have
• Be more alive and professional
Should not have
• Any other colours besides the ones in the logos

```html
<!DOCTYPE html>
<html lang="en">
<head>
<meta charset="utf-8">
<title>Korbel Ridge Letterhead</title>
<link href="https://fonts.googleapis.com/css2?family=Open+Sans:wght@400;600;700&display=swap" rel="stylesheet">
<style>
  :root {
    --backdrop: #eceded;
    --paper: #ffffff;
    --ink: #1e2226;
    --brand-red: #8e1f1c;
    --footer-black: #151719;
    --footer-text: #e8e8e8;
    --muted: #3a3d40;
  }
  * { box-sizing: border-box; margin: 0; padding: 0; }
  html, body { width: 1200px; height: 800px; overflow: hidden; }
  body {
    background: var(--backdrop);
    font-family: "Open Sans", Arial, sans-serif;
    color: var(--ink);
    position: relative;
  }
  .letterhead {
    position: absolute;
    left: 331px; top: 20px;
    width: 538px; height: 760px;
    background: var(--paper);
    box-shadow: 0 2px 10px rgba(0,0,0,0.12);
  }
  .top-rule { position: absolute; left: 0; right: 0; height: 1.5px; }
  .top-rule--dark { top: 22px; background: var(--ink); }
  .top-rule--red { top: 26px; background: var(--brand-red); }
  .tagline {
    position: absolute; right: 28px; top: 38px;
    text-align: right;
    font-size: 6.2px; font-weight: 600; letter-spacing: 0.6px;
    line-height: 1.35; text-transform: uppercase; color: var(--muted);
  }
  .tagline strong { color: var(--brand-red); font-weight: 700; }
  .brand-name {
    position: absolute; left: 36px; top: 78px;
    font-size: 26px; font-weight: 700; letter-spacing: 0.5px;
    color: var(--ink);
  }
  .letter-body {
    position: absolute; left: 52px; right: 40px; top: 150px;
    font-size: 8.8px; line-height: 1.42; letter-spacing: 0.2px;
    text-align: justify;
  }
  .letter-body p { margin-bottom: 10px; }
  .sign-off { margin-top: 20px; }
  .sign-off p { margin-bottom: 26px; }
  .footer {
    position: absolute; left: 0; right: 0; bottom: 14px; height: 140px;
  }
  .footer-rule { position: absolute; left: 0; right: 0; height: 1.5px; }
  .footer-rule--dark { top: 0; background: var(--ink); }
  .footer-rule--red { top: 4px; background: var(--brand-red); }
  .footer-band {
    position: absolute; left: 0; right: 0; top: 10px; bottom: 5px;
    background: var(--footer-black);
    display: flex; align-items: center;
    padding: 0 12px;
    color: var(--footer-text);
    font-size: 7.6px; line-height: 1.4;
  }
  .footer-column { flex: 1; padding: 0 12px; white-space: nowrap; }
  .footer-column + .footer-column { border-left: 1px solid var(--footer-text); }
  .footer-column .contact { font-weight: 700; margin-top: 4px; }
  .footer-column--directors { text-align: center; flex: 1.1; }
  .footer-column--directors .registration { text-align: right; margin-bottom: 8px; }
  .footer-column--directors .directors-label,
  .footer-column--directors .director { font-weight: 700; }
  .bottom-rule { position: absolute; left: 0; right: 0; bottom: 0; height: 1.5px; background: var(--brand-red); }
</style>
</head>
<body>
  <main class="letterhead">
    <div class="top-rule top-rule--dark"></div>
    <div class="top-rule top-rule--red"></div>

    <div class="tagline">Building lasting<br>value on every site<br>with care, <strong>every day</strong></div>

    <div class="brand-name">KORBEL RIDGE</div>

    <section class="letter-body">
      <p>Dear :</p>
      <p>Lorem ipsum dolor sit amet, consectetur adipiscing elit. Aenean ut ipsum eget massa hendrerit vestibulum vel in velit. Donec pretium neque velit.</p>
      <p>Aliquam porta lectus nec mauris ornare venenatis. Vivamus non est turpis, et cursus sem. Mauris vehicula erat in diam auctor at bibendum nisl lacinia.</p>
      <p>Morbi imperdiet neque vehicula nunc convallis gravida. Vestibulum iaculis pretium placerat. Integer consequat, est sit amet facilisis eleifend, nibh nibh varius orci, eget dapibus arcu dui non purus. Pellentesque in magna mauris. Duis enim sapien, dictum vitae condimentum a, pulvinar vel lacus. Mauris et molestie nibh. Vestibulum vitae nulla at metus elementum porta sit amet interdum elit. Nulla sollicitudin fringilla volutpat congue.</p>
      <p>Nunc eu velit id dapibus fermentum, turpis sapien ornare dui, ac congue purus. Nunc sed ante dui, in porta lectus. Cras nec habitasse platea dictumst. Maecenas id diam quis dui porta felis. Donec ullamcorper mattis posuere. Phasellus vel dapibus. Vestibulum ante ipsum.</p>
      <p>Nunc eu velit id dapibus fermentum, turpis sapien ornare dui, ac congue purus. Nunc sed ante dui, in porta lectus. Cras nec habitasse platea dictumst. Maecenas id diam quis dui porta felis. Donec ullamcorper mattis posuere. Phasellus vel dapibus. Vestibulum ante ipsum.</p>
      <div class="sign-off">
        <p>Yours sincerely,</p>
        <p>Signature</p>
      </div>
    </section>

    <footer class="footer">
      <div class="footer-rule footer-rule--dark"></div>
      <div class="footer-rule footer-rule--red"></div>
      <div class="footer-band">
        <div class="footer-column">
          Korbel Ridge JV (Pty) Limited<br>
          12 Marsh Road Linden,<br>
          Johannesburg<br>
          PO Box 55120, Parkhurst, 2193<br>
          South Africa
          <div class="contact">T: +27 (0)11 555 0142<br>www.korbelridge.co.za</div>
        </div>
        <div class="footer-column">
          Korbel Ridge Build JV (Pty) Limited<br>
          27 Acacia Road, Cnr Oak<br>
          Avenue Rosebank West,<br>
          Johannesburg 2196<br>
          South Africa
          <div class="contact">T: +27 (0)11 555 0187<br>www.ridgelinebuild.co.za</div>
        </div>
        <div class="footer-column footer-column--directors">
          <div class="registration">Registration No. 2017/402615/07<br>Trading as Korbel Ridge JV (Pty) Limited</div>
          <div class="directors-label">Directors:</div>
          <div class="director">Martin Cole</div>
          <div class="director">Peter Ndlovu</div>
        </div>
      </div>
      <div class="bottom-rule"></div>
    </footer>
  </main>
</body>
</html>
```